Psychotherapy Website - Based in London

I am a newly trained psychotherapist and need a new website for www.rosalindfaber.co.uk.

I offer therapy for addiction, relationships, trauma and many other issues people face in their lives.

I want the website to be welcoming, gentle, feminine and for people to feel safe.

I do not like a page site that scrolls through sections, rather each page should be separate. Here some examples that i like. Sectional rather than scrolled.

https://www.hettiemarsh.com/
https://www.thequietwardrooms.com/

The imagery should be around pink using the flower in the logo / wording and around the site:

Here is a link to the flower for ideas:
https://www.pictofind.net/search?q=pink+gerbera&rlz=2D4KQTW_en-GBGB415GB415&source=lnms&tbm=isch&sa=X&ved=7cvQRtrk482h3PxZTuKLmeNBwXW_1AtXpVlKDbOQBmFLB&biw=1500&bih=889&dpr=2

RosalindFaber
Compassionate Psychotherapy

Is the logo and subheader for the website. Please use a typeface for the name that is appealing and professional.

Type face similar NOT EXLUSIVLY - JUST AN IDEA like this:
https://glowtonicstudio.com/

Basic business card i created as a rough idea below.

I have also added the website copy.

The headers are

Homepage
About Me
Therapy
Common Questions
Blog
Contact Me

Target Market(s)

Clients who are dealing with stress, trauma, pain, addiction

Industry/Entity Type

Therapy and Psychology

Coding

Coded - Design and coding required

Number of Pages Required

5+ page

Font styles to use
Serif
Sans Serif
Script

Colors
0054AA
0677BA
7BADD7
CADEEF
E8F1F8
0094D4
00A9DD
6FCCEA
C7EBF8
E9F6FB
E54698
E96AAD
F1A4CE
F9D9EA
FCEFF6

Requirements
Must have
• Pink Gerbera Flower integrated into design
Nice to have
• Images but not to stock imagery. Needs to look authentic and natural
Should not have
• Stock images of people. Images are important but needs to feel REAL

```html
<!DOCTYPE html>
<html lang="en">
<head>
<meta charset="utf-8">
<title>Rosalind Faber – Compassionate Psychotherapy – Website Presentation</title>
<link rel="stylesheet" href="https://fonts.googleapis.com/css2?family=Cinzel:wght@400;500&family=Tinos:wght@400;700&display=swap">
<style>
:root{
  --magenta:#fb0a80;
  --pink:#e54698;
  --pink-mid:#e96aad;
  --pink-soft:#f1a4ce;
  --pink-pale:#f9d9ea;
  --pink-mist:#fceff6;
  --ink:#2a2a2a;
  --grey:#6d6a6c;
  --panel:#f2f0f1;
  --white:#ffffff;
}
*{box-sizing:border-box;margin:0;padding:0}
html,body{width:1200px;height:1200px;overflow:hidden}
body{background:var(--magenta);font-family:'Tinos',serif}
.board{position:relative;width:1200px;height:1200px;overflow:hidden;background:var(--magenta)}

/* brand band */
.brand-band{position:absolute;left:0;top:58px;width:755px;height:210px;
  background:linear-gradient(90deg,#ff5aa8 0%,#ffd6ea 14%,#fff 30%,#fff 100%)}
.brand-mark{position:absolute;left:314px;top:35px;width:76px;height:76px;border-radius:50%;background:var(--pink)}
.brand-name{position:absolute;left:0;width:705px;top:118px;text-align:center;
  font:400 44px 'Cinzel',serif;color:var(--ink);letter-spacing:1px}
.brand-tagline{position:absolute;left:0;width:705px;top:166px;text-align:center;
  font:400 11px 'Tinos',serif;letter-spacing:4.5px;color:var(--ink)}

/* screens */
.screen{position:absolute;overflow:hidden;background:var(--white);box-shadow:0 2px 8px rgba(0,0,0,.18)}
.screen>.page{transform-origin:0 0}
.screen-hero{left:45px;top:327px;width:660px;height:363px}
.screen-hero>.page{transform:scale(.66)}
.screen-about{left:45px;top:734px;width:310px;height:181px}
.screen-therapy{left:395px;top:734px;width:310px;height:181px}
.screen-faq{left:45px;top:958px;width:310px;height:182px}
.screen-contact{left:395px;top:958px;width:310px;height:182px}
.screen-small>.page{transform:scale(.31)}
.screen-full{left:757px;top:41px;width:336px;height:1118px}
.screen-full>.page{transform:scale(.336)}

/* page */
.page{width:1000px;background:var(--white);color:var(--grey);font-family:'Tinos',serif}
.site-nav{position:relative;z-index:2;height:70px;display:flex;align-items:center;justify-content:center;gap:62px;
  background:linear-gradient(#fff,#fdf1f7);font:700 13px 'Tinos',serif;letter-spacing:.6px;color:#7a7678}
.site-nav .active{color:var(--pink)}
.nav-mark{position:relative;width:64px;height:64px;margin-top:14px;border-radius:50%;background:#fdf1f7;display:flex;align-items:center;justify-content:center}
.nav-mark span{width:40px;height:40px;border-radius:50%;background:var(--pink)}

.hero{position:relative;height:294px}
.hero-image{position:absolute;inset:0;
  background:radial-gradient(ellipse at 58% 55%,#f4bcd2 0%,#eea5c5 25%,#f6c6dc 55%,#fbe3ee 100%)}
.hero-title{position:absolute;left:0;right:0;top:112px;text-align:center;font:400 58px 'Cinzel',serif;color:var(--white);letter-spacing:1px}
.hero-tagline{position:absolute;left:0;right:0;top:186px;text-align:center;font:400 15px 'Tinos',serif;letter-spacing:7px;color:var(--white)}

.intro{height:446px;padding-top:40px;text-align:center;
  background:radial-gradient(circle at 8% 35%,#f6f1f3 0,#fff 30%)}
.intro-quote{font:700 23px 'Tinos',serif;color:var(--pink);letter-spacing:.5px}
.intro-box{width:760px;margin:36px auto 0;padding:14px 40px;background:#f6f5f6;border-radius:6px;box-shadow:0 3px 8px rgba(0,0,0,.15)}
.intro-box p{font-size:13px;line-height:1.5;padding:6px 0;border-bottom:1px solid #d9d6d8;color:#6f6c6e}
.intro-box p:first-child{font-size:16px}
.intro-box p:nth-child(2){font-size:15px}
.intro-box p:last-child{border-bottom:none}

.section-title{display:inline-block;font:700 16px 'Tinos',serif;color:var(--pink);letter-spacing:1px;border-bottom:2px solid var(--pink-soft);padding-bottom:4px}
.body-text{font-size:12.5px;line-height:1.6;color:#6f6c6e}
.body-text+.body-text{margin-top:12px}

.about{position:relative;height:452px;background:var(--panel);padding:54px 0 0 160px}
.about-text{width:330px;margin-top:20px}
.portrait-block{position:absolute;left:610px;top:176px;width:240px;height:230px;background:var(--pink-mid)}
.portrait-block-top{position:absolute;left:560px;top:60px;width:40px;height:40px;background:var(--pink-mid)}
.portrait-frame{position:absolute;left:575px;top:70px;width:250px;height:300px;background:var(--white);padding:10px;box-shadow:0 3px 8px rgba(0,0,0,.2)}
.portrait{width:100%;height:100%;background:linear-gradient(160deg,#f4f2f1 0%,#e9dfd8 45%,#e58aa9 100%)}

.therapy{position:relative;height:744px;padding:58px 160px 0}
.floral{position:absolute;border-radius:50%;background:radial-gradient(circle,#f6b3cc 0%,#fbd8e6 45%,rgba(255,255,255,0) 72%)}
.floral-left{left:-10px;top:-20px;width:170px;height:160px}
.floral-right{right:-20px;top:540px;width:200px;height:200px}
.therapy .body-text{margin-top:14px}
.help-heading{text-align:center;margin-top:30px}
.help-heading span{display:inline-block;font:400 16px 'Tinos',serif;color:var(--pink);letter-spacing:1px;padding:0 12px 6px;border-bottom:2px solid var(--pink-soft)}
.help-list{list-style:none;display:grid;grid-template-columns:repeat(3,1fr);grid-auto-flow:column;grid-template-rows:repeat(9,auto);row-gap:11px;margin-top:26px;font-size:12px;color:#6f6c6e}
.help-list li{position:relative;padding-left:26px}
.help-list li::before{content:"";position:absolute;left:4px;top:1px;width:5px;height:9px;border:solid var(--pink-mid);border-width:0 2px 2px 0;transform:rotate(45deg)}

.faq{height:366px;padding-top:56px;text-align:center}
.faq-list{width:680px;margin:24px auto 0;text-align:left}
.faq-item{margin-bottom:10px}
.faq-head{display:flex;justify-content:space-between;align-items:center;height:26px;padding:0 12px;background:var(--pink);color:var(--white);font:700 11px 'Tinos',serif;letter-spacing:.4px}
.faq-head b{font-size:18px;font-weight:700}
.faq-body{border:1px solid var(--pink);border-top:none;padding:14px 12px;font-size:11px;line-height:1.5;color:#6f6c6e}
.faq-body p+p{margin-top:8px}

.blog{height:491px;background:linear-gradient(#fde6f0,#fcd9e8);padding-top:40px;text-align:center}
.blog-card{width:740px;margin:24px auto 0;background:var(--white);border-radius:8px;padding:22px 26px;display:flex;gap:24px;box-shadow:0 3px 8px rgba(0,0,0,.12)}
.blog-post{flex:1;border-radius:10px;box-shadow:0 2px 6px rgba(0,0,0,.15);overflow:hidden;padding-bottom:12px}
.blog-image{height:170px}
.blog-image.one{background:linear-gradient(150deg,#f8d6e3,#f1bfcf 60%,#fae8ee)}
.blog-image.two{background:radial-gradient(circle at 50% 55%,#f08cb4,#f7c2d8 60%,#fbe0ec)}
.blog-image.three{background:linear-gradient(160deg,#fbe2ec,#f2b6cc 70%,#f7d3e1)}
.blog-post h3{font:700 14px 'Tinos',serif;color:var(--pink);margin-top:10px}
.blog-post p{font-size:9px;line-height:1.4;padding:4px 14px 0;color:#8a8688}
.read-more{display:inline-block;margin-top:28px;background:var(--white);color:var(--pink);font:700 12px 'Tinos',serif;padding:8px 28px;border-radius:3px;box-shadow:0 2px 4px rgba(0,0,0,.12)}

.contact{position:relative;height:417px;background:radial-gradient(circle at 70% 40%,#f1eff0,#ececec 70%);padding:50px 160px 0}
.contact .body-text{margin-top:14px}
.contact-list{list-style:none;margin-top:22px;width:300px}
.contact-list li{position:relative;padding-left:30px;margin-bottom:16px;font-size:11.5px;line-height:1.45;color:#6f6c6e}
.contact-list h4{font:700 12px 'Tinos',serif;color:var(--pink)}
.contact-list svg{position:absolute;left:0;top:0;width:14px;height:14px;fill:#7a7678}
.map{position:absolute;left:545px;top:150px;width:370px;height:230px;border-radius:4px;
  background:linear-gradient(150deg,#eef0ec 0%,#e4e9e2 45%,#b9d3e6 62%,#e8ebe6 75%)}
.site-footer{height:47px;background:var(--magenta);display:flex;align-items:center;justify-content:space-between;padding:0 60px 0 130px;color:var(--white);font-size:11px}
.footer-social{display:flex;gap:18px}
.footer-social span{width:12px;height:12px;border-radius:50%;background:var(--white)}
</style>
</head>
<body>
<main class="board">

  <header class="brand-band">
    <span class="brand-mark"></span>
    <div class="brand-name">Rosalind Faber</div>
    <div class="brand-tagline">COMPASSIONATE PSYCHOTHERAPY</div>
  </header>

  <!-- home page hero -->
  <section class="screen screen-hero">
    <div class="page">
      <nav class="site-nav"><span class="active">HOME</span><span>ABOUT ME</span><span>THERAPY</span><span class="nav-mark"><span></span></span><span>FREQUENT QUESTIONS</span><span>BLOG</span><span>CONTACT ME</span></nav>
      <div class="hero">
        <div class="hero-image" role="img" aria-label="Soft close-up photograph of a pink gerbera flower"></div>
        <div class="hero-title">Rosalind Faber</div>
        <div class="hero-tagline">COMPASSIONATE PSYCHOTHERAPY</div>
      </div>
      <div class="intro">
        <h2 class="intro-quote">"MAKE A POSITIVE CHANGE IN YOUR LIFE TODAY"</h2>
        <div class="intro-box">
          <p>Taking the first steps towards engaging in therapy can be a very personal journey.</p>
          <p>Whilst, it can be challenging, I will ensure to make this journey as safe and as comfortable for you as possible.</p>
        </div>
      </div>
    </div>
  </section>

  <!-- about page -->
  <section class="screen screen-small screen-about">
    <div class="page">
      <nav class="site-nav"><span class="active">HOME</span><span>ABOUT ME</span><span>THERAPY</span><span class="nav-mark"><span></span></span><span>FREQUENT QUESTIONS</span><span>BLOG</span><span>CONTACT ME</span></nav>
      <div class="about">
        <h2 class="section-title">ABOUT ME</h2>
        <div class="about-text">
          <p class="body-text">I have over 30 year's experience of dealing with addictions. Addictions are often more of a solution to fear and emotional pain. However, eventually the addiction causes more problems. I know recovery is possible with the right support.</p>
          <p class="body-text">I have also had some twenty years of experience of dealing with mental health issues such as depression, anxiety, complex PTSD and trauma. It is possible to manage these issues and live a full life.</p>
          <p class="body-text">I have worked in the voluntary sector as a listener and I am currently a therapist for a local charity.</p>
        </div>
        <span class="portrait-block-top"></span>
        <span class="portrait-block"></span>
        <div class="portrait-frame"><div class="portrait" role="img" aria-label="Portrait photograph of the therapist"></div></div>
      </div>
    </div>
  </section>

  <!-- therapy page -->
  <section class="screen screen-small screen-therapy">
    <div class="page">
      <nav class="site-nav"><span class="active">HOME</span><span>ABOUT ME</span><span>THERAPY</span><span class="nav-mark"><span></span></span><span>FREQUENT QUESTIONS</span><span>BLOG</span><span>CONTACT ME</span></nav>
      <div class="therapy">
        <div class="floral floral-left" role="img" aria-label="Watercolour pink flower decoration"></div>
        <h2 class="section-title">THERAPY</h2>
        <p class="body-text">There are times when the challenges of life can make us feel overwhelmed and isolated, and it may feel difficult to talk about how we feel to those who are closest to us. We go through transitions and crises and experience uncertainty and loss. How we deal with difficulties in life is an important aspect in how we carry on forwards and ultimately who we become as people. I offer a range of psychotherapeutic approaches including transactional analysis and relational therapy.</p>
        <p class="body-text">Through the process of exploration, we enable self-knowledge and self-awareness to help you grow and conquer issues that may previously have been experienced as all-consuming or overwhelming. We will not only look at your problems in the present but also identify the roots of those problems from your past, and explore how past experiences may have affected the way you live today.</p>
        <p class="body-text">Therapy can help you to develop ways of coping better and overcoming issues you may feel are holding you back. I can help you find and develop your personal strengths and help identify what is meaningful to you in life.</p>
        <div class="help-heading"><span>WHAT WE CAN HELP WITH</span></div>
        <ul class="help-list">
          <li>Addiction</li><li>Bullying</li><li>Depression</li><li>Fear</li><li>Grief</li><li>Loss Of Meaning</li><li>Problems With Motivation/Focus</li><li>Self Sabotage</li><li>Stress</li>
          <li>Anger</li><li>Career Changes</li><li>Difficulty Making Decisions</li><li>Feeling Alone/Isolated</li><li>Identity Issues</li><li>LGBT Issues</li><li>Psychosis</li><li>Sexual Abuse</li><li>Substance Misuse</li>
          <li>Anxiety</li><li>Crisis/Breakdown</li><li>Emotional Abuse</li><li>Health Issues</li><li>Low Self Confidence</li><li>Negative Thinking</li><li>Relationship Problems</li><li>Sexuality</li>
        </ul>
      </div>
    </div>
  </section>

  <!-- questions page -->
  <section class="screen screen-small screen-faq">
    <div class="page">
      <nav class="site-nav"><span class="active">HOME</span><span>ABOUT ME</span><span>THERAPY</span><span class="nav-mark"><span></span></span><span>FREQUENT QUESTIONS</span><span>BLOG</span><span>CONTACT ME</span></nav>
      <div class="faq">
        <h2 class="section-title">FREQUENT QUESTIONS</h2>
        <div class="faq-list">
          <div class="faq-item"><div class="faq-head">HOW LONG WILL I NEED THERAPY FOR?<b>–</b></div>
            <div class="faq-body"><p>Therapy can last anywhere from six sessions to several months or even years. It will depend on what you want to explore. Some people come to therapy with a very specific problem and a few sessions may be sufficient.</p><p>Other people come to therapy with more complicated issues they are struggling with and may feel they need a few months or more to understand and resolve their issues. Many people come with long-standing patterns and find longer work helpful.</p></div></div>
          <div class="faq-item"><div class="faq-head">HOW LONG ARE THE SESSIONS?<b>+</b></div></div>
          <div class="faq-item"><div class="faq-head">HOW MUCH IS EACH SESSION?<b>+</b></div></div>
        </div>
      </div>
      <div class="blog">
        <h2 class="section-title">LATEST FROM BLOG</h2>
        <div class="blog-card">
          <article class="blog-post"><div class="blog-image one" role="img" aria-label="Photograph of hands with pink nails"></div><h3>Trauma And The Bears</h3><p>A short reflection on how early fear shapes the way we respond to stress later in life.</p></article>
          <article class="blog-post"><div class="blog-image two" role="img" aria-label="Photograph of a pink gerbera flower"></div><h3>Trauma And The Bears</h3><p>A short reflection on how early fear shapes the way we respond to stress later in life.</p></article>
          <article class="blog-post"><div class="blog-image three" role="img" aria-label="Photograph of a dancer on a pink background"></div><h3>Trauma And The Bears</h3><p>A short reflection on how early fear shapes the way we respond to stress later in life.</p></article>
        </div>
      </div>
    </div>
  </section>

  <!-- contact page -->
  <section class="screen screen-small screen-contact">
    <div class="page">
      <nav class="site-nav"><span class="active">HOME</span><span>ABOUT ME</span><span>THERAPY</span><span class="nav-mark"><span></span></span><span>FREQUENT QUESTIONS</span><span>BLOG</span><span>CONTACT ME</span></nav>
      <div class="contact">
        <h2 class="section-title">CONTACT ME</h2>
        <p class="body-text">If you have any questions, please do not hesitate to contact us on the mentioned address, e-mail address or phone number.</p>
        <ul class="contact-list">
          <li><svg viewBox="0 0 14 14"><path d="M7 0a5 5 0 0 0-5 5c0 4 5 9 5 9s5-5 5-9a5 5 0 0 0-5-5zm0 7a2 2 0 1 1 0-4 2 2 0 0 1 0 4z"/></svg><h4>Address</h4>Larkfield Community Hall, 8 Willow Row<br>East Marston, TW9 4QT</li>
          <li><svg viewBox="0 0 14 14"><path d="M3 1l2.5 3-1.5 1.5c1 2 2.5 3.5 4.5 4.5L10 8.5 13 11l-1.5 2C6 12.5 1.5 8 1 2.5z"/></svg><h4>Contact Us</h4>07700 900481</li>
          <li><svg viewBox="0 0 14 14"><path d="M7 0a7 7 0 1 0 0 14A7 7 0 0 0 7 0zm0 1.5c.8 1 1.4 2.6 1.5 4.5h-3C5.6 4.1 6.2 2.5 7 1.5zM1.6 8h2.9c.1 1.7.6 3.2 1.3 4.3A5.6 5.6 0 0 1 1.6 8zm6.6 4.3c.7-1.1 1.2-2.6 1.3-4.3h2.9a5.6 5.6 0 0 1-4.2 4.3z"/></svg><h4>Website</h4>www.rosalindfaber.co.uk</li>
          <li><svg viewBox="0 0 14 14"><path d="M0 3h14v8H0zm1 1l6 4 6-4"/></svg><h4>E-Mail</h4>hello@rosalindfaber.co.uk</li>
        </ul>
        <div class="map" role="img" aria-label="Street map showing the practice location"></div>
      </div>
      <footer class="site-footer"><span>Copyright © 2021 All Rights Reserved.</span><span class="footer-social"><span></span><span></span><span></span><span></span></span></footer>
    </div>
  </section>

  <!-- full home page -->
  <section class="screen screen-full">
    <div class="page">
      <nav class="site-nav"><span class="active">HOME</span><span>ABOUT ME</span><span>THERAPY</span><span class="nav-mark"><span></span></span><span>FREQUENT QUESTIONS</span><span>BLOG</span><span>CONTACT ME</span></nav>
      <div class="hero">
        <div class="hero-image" role="img" aria-label="Soft close-up photograph of a pink gerbera flower"></div>
        <div class="hero-title">Rosalind Faber</div>
        <div class="hero-tagline">COMPASSIONATE PSYCHOTHERAPY</div>
      </div>
      <div class="intro">
        <h2 class="intro-quote">"MAKE A POSITIVE CHANGE IN YOUR LIFE TODAY"</h2>
        <div class="intro-box">
          <p>Taking the first steps towards engaging in therapy can be a very personal journey.</p>
          <p>Whilst, it can be challenging, I will ensure to make this journey as safe and as comfortable for you as possible.</p>
          <p>Psychotherapy can help you see your current situation in new light, depth and clarity. It can change old and unhelpful perspectives and feelings about yourself and your life, and ultimately help you make positive changes.</p>
          <p>I provide a real non-judgemental space where any issues can be explored in complete confidentiality.</p>
          <p>My practice is based locally, where the room is homely, comfortable and welcoming. I believe a good environment contributes to great therapy.</p>
          <p>Alternatively, I am also available to provide therapy online, if this environment is more accommodating for my clients. I am passionate about improving mental health and committed to offering therapy to all individuals regardless of their age, race, culture or background.</p>
        </div>
      </div>
      <div class="about">
        <h2 class="section-title">ABOUT ME</h2>
        <div class="about-text">
          <p class="body-text">I have over 30 year's experience of dealing with addictions. Addictions are often more of a solution to fear and emotional pain. However, eventually the addiction causes more problems. I know recovery is possible with the right support.</p>
          <p class="body-text">I have also had some twenty years of experience of dealing with mental health issues such as depression, anxiety, complex PTSD and trauma. It is possible to manage these issues and live a full life.</p>
          <p class="body-text">I have worked in the voluntary sector as a listener and I am currently a therapist for a local charity.</p>
        </div>
        <span class="portrait-block-top"></span>
        <span class="portrait-block"></span>
        <div class="portrait-frame"><div class="portrait" role="img" aria-label="Portrait photograph of the therapist"></div></div>
      </div>
      <div class="therapy">
        <div class="floral floral-left" role="img" aria-label="Watercolour pink flower decoration"></div>
        <div class="floral floral-right" role="img" aria-label="Watercolour pink flower decoration"></div>
        <h2 class="section-title">THERAPY</h2>
        <p class="body-text">There are times when the challenges of life can make us feel overwhelmed and isolated, and it may feel difficult to talk about how we feel to those who are closest to us. We go through transitions and crises and experience uncertainty and loss. How we deal with difficulties in life is an important aspect in how we carry on forwards and ultimately who we become as people. I offer a range of psychotherapeutic approaches including transactional analysis and relational therapy.</p>
        <p class="body-text">Through the process of exploration, we enable self-knowledge and self-awareness to help you grow and conquer issues that may previously have been experienced as all-consuming or overwhelming. We will not only look at your problems in the present but also identify the roots of those problems from your past, and explore how past experiences may have affected the way you live today.</p>
        <p class="body-text">Therapy can help you to develop ways of coping better and overcoming issues you may feel are holding you back. I can help you find and develop your personal strengths and help identify what is meaningful to you in life.</p>
        <div class="help-heading"><span>WHAT WE CAN HELP WITH</span></div>
        <ul class="help-list">
          <li>Addiction</li><li>Bullying</li><li>Depression</li><li>Fear</li><li>Grief</li><li>Loss Of Meaning</li><li>Problems With Motivation/Focus</li><li>Self Sabotage</li><li>Stress</li>
          <li>Anger</li><li>Career Changes</li><li>Difficulty Making Decisions</li><li>Feeling Alone/Isolated</li><li>Identity Issues</li><li>LGBT Issues</li><li>Psychosis</li><li>Sexual Abuse</li><li>Substance Misuse</li>
          <li>Anxiety</li><li>Crisis/Breakdown</li><li>Emotional Abuse</li><li>Health Issues</li><li>Low Self Confidence</li><li>Negative Thinking</li><li>Relationship Problems</li><li>Sexuality</li>
        </ul>
      </div>
      <div class="faq">
        <h2 class="section-title">FREQUENT QUESTIONS</h2>
        <div class="faq-list">
          <div class="faq-item"><div class="faq-head">HOW LONG WILL I NEED THERAPY FOR?<b>–</b></div>
            <div class="faq-body"><p>Therapy can last anywhere from six sessions to several months or even years. It will depend on what you want to explore. Some people come to therapy with a very specific problem and a few sessions may be sufficient.</p><p>Other people come to therapy with more complicated issues they are struggling with and may feel they need a few months or more to understand and resolve their issues. Many people come with long-standing patterns and find longer work helpful.</p></div></div>
          <div class="faq-item"><div class="faq-head">HOW LONG ARE THE SESSIONS?<b>+</b></div></div>
          <div class="faq-item"><div class="faq-head">HOW MUCH IS EACH SESSION?<b>+</b></div></div>
        </div>
      </div>
      <div class="blog">
        <h2 class="section-title">LATEST FROM BLOG</h2>
        <div class="blog-card">
          <article class="blog-post"><div class="blog-image one" role="img" aria-label="Photograph of hands with pink nails"></div><h3>Trauma And The Bears</h3><p>A short reflection on how early fear shapes the way we respond to stress later in life.</p></article>
          <article class="blog-post"><div class="blog-image two" role="img" aria-label="Photograph of a pink gerbera flower"></div><h3>Trauma And The Bears</h3><p>A short reflection on how early fear shapes the way we respond to stress later in life.</p></article>
          <article class="blog-post"><div class="blog-image three" role="img" aria-label="Photograph of a dancer on a pink background"></div><h3>Trauma And The Bears</h3><p>A short reflection on how early fear shapes the way we respond to stress later in life.</p></article>
        </div>
        <span class="read-more">Read More</span>
      </div>
      <div class="contact">
        <h2 class="section-title">CONTACT ME</h2>
        <p class="body-text">If you have any questions, please do not hesitate to contact us on the mentioned address, e-mail address or phone number.</p>
        <ul class="contact-list">
          <li><svg viewBox="0 0 14 14"><path d="M7 0a5 5 0 0 0-5 5c0 4 5 9 5 9s5-5 5-9a5 5 0 0 0-5-5zm0 7a2 2 0 1 1 0-4 2 2 0 0 1 0 4z"/></svg><h4>Address</h4>Larkfield Community Hall, 8 Willow Row<br>East Marston, TW9 4QT</li>
          <li><svg viewBox="0 0 14 14"><path d="M3 1l2.5 3-1.5 1.5c1 2 2.5 3.5 4.5 4.5L10 8.5 13 11l-1.5 2C6 12.5 1.5 8 1 2.5z"/></svg><h4>Contact Us</h4>07700 900481</li>
          <li><svg viewBox="0 0 14 14"><path d="M7 0a7 7 0 1 0 0 14A7 7 0 0 0 7 0zm0 1.5c.8 1 1.4 2.6 1.5 4.5h-3C5.6 4.1 6.2 2.5 7 1.5zM1.6 8h2.9c.1 1.7.6 3.2 1.3 4.3A5.6 5.6 0 0 1 1.6 8zm6.6 4.3c.7-1.1 1.2-2.6 1.3-4.3h2.9a5.6 5.6 0 0 1-4.2 4.3z"/></svg><h4>Website</h4>www.rosalindfaber.co.uk</li>
          <li><svg viewBox="0 0 14 14"><path d="M0 3h14v8H0zm1 1l6 4 6-4"/></svg><h4>E-Mail</h4>hello@rosalindfaber.co.uk</li>
        </ul>
        <div class="map" role="img" aria-label="Street map showing the practice location"></div>
      </div>
      <footer class="site-footer"><span>Copyright © 2021 All Rights Reserved.</span><span class="footer-social"><span></span><span></span><span></span><span></span></span></footer>
    </div>
  </section>

</main>
</body>
</html>
```